Guaranteed Job - Sleek Sexy Business Card UV Spot

Im looking for a sleek and sexy business card, that resembles elite or VIP status status.
our business is corinvale.example
you can view our products on there, but our main audience for handing out our cards will be for people in the hospitality industry, so it will need to impress high management and CEO of hotels and restaurants, bars, clubs etc...
the card features will have UV spot on both sides, 400gsm stock. standard size.
Artwork should be 86 x 54mm + 2mm bleed = 90 x 58mm
it should have a nice "unique" uv spot pattern that highlights the card, not a repeated pattern, theres no originality there, and it will be disregarded.
The written material will be:
Corin Vale Hospitality College (logo)
Tobin Marsh
Director
Phone: 1300 615 737
Mobile: 0455 817 296
Email: info@corinvale.example
website: www.corinvale.example
I'm looking for originality here, i don't want just a simple stock card, want something that has a wow factor for people.
You will find the logo attached. you may invert the white to black words to suit the background as you please.
thank you and good luck
As a side note, ive received a lot of proposals, im too busy to give feedback to each and every one, so if i havent provided feedback for your design within 24 hours, then consider it not acceptable, and you could resubmit another design.
So far i have not seen any design that stood out for me, they all seem pretty generic. there nothing thats unique, i would figure for the amount that im offering, that people would put some more effort and creativity into the design.
so far over 200 designs submitted, and nothing i have seen looks very original, everything looks like a different variation of the same stuff, i said it very clearly i wanted something unique, the only thing that has come close to it so far is this one
Reason: Ive received alot of design concepts and i have reviewed everyone, but i havent had time to give feedback to every single one, only the ones that have interested me, if i havent responded, its because i havent found it good enough.
so far only a few design have been on par with what ive been looking for, an attractive eye popping design.
heres a few of them,
http://files.pixelbazaar.example/design_img/51736/62418/62418_2840915_51736_image.jpg
http://files.pixelbazaar.example/design_img/51736/68254/68254_2841377_51736_image.jpg
theyre, both unique and original, and eye catching, the only thing theyre missing is the sexyness.
if you still think you have some creativity left in your minds, then throw it on here.
Reason: Sorry guys for the delay, I was in a serious accident and out of commission for the past few months, I'm just slowly recovering now, please bare with me as i try to attend to this project, it may take me awhile as I have other projects that are on standby, I'm not 100% at the moment, so im extending the deadline for 2 weeks right now. Thanks for your patience.
Hospitality

```html
<!DOCTYPE html>
<html lang="en">
<head>
<meta charset="utf-8">
<title>Corin Vale Hospitality College – Business Card</title>
<link rel="stylesheet" href="https://fonts.googleapis.com/css2?family=Oswald:wght@400;600;700&display=swap">
<style>
  :root {
    --backdrop: #e9e6e1;
    --card-black: #141414;
    --card-edge: #262626;
    --gloss: rgba(255,255,255,0.10);
    --ink-white: #ffffff;
    --ink-black: #111111;
    --accent-blue: #4fa9d6;
    --muted: #cfcfcf;
  }
  * { box-sizing: border-box; margin: 0; padding: 0; }
  html, body {
    width: 1200px; height: 1000px; overflow: hidden;
    background: var(--backdrop);
    font-family: "Oswald", "Arial Narrow", sans-serif;
  }
  .sheet {
    position: relative; width: 1200px; height: 1000px;
    display: flex; justify-content: center; align-items: center; gap: 70px;
  }
  .card {
    position: relative; width: 500px; height: 796px;
    background:
      linear-gradient(100deg, transparent 30%, var(--gloss) 48%, transparent 66%),
      radial-gradient(ellipse at 50% 45%, #2a2a2a 0%, var(--card-black) 70%);
    border: 1px solid var(--card-edge);
    border-radius: 6px;
    box-shadow: 0 18px 40px rgba(0,0,0,0.28);
    overflow: hidden;
    text-transform: uppercase;
  }

  /* Front */
  .front-mark {
    position: absolute; top: 250px; left: 0; right: 0;
    text-align: center; color: var(--ink-white);
    font-weight: 700; font-size: 84px; line-height: 0.95; letter-spacing: 1px;
  }
  .front-label {
    position: absolute; left: 0; bottom: 70px;
    background: var(--ink-white); color: var(--ink-black);
    padding: 12px 26px 12px 30px;
    font-weight: 700; line-height: 1;
  }
  .front-label .label-name { display: block; font-size: 40px; letter-spacing: 0.5px; }
  .front-label .label-sub { display: block; font-size: 20px; letter-spacing: 1px; margin-top: 6px; }

  /* Back */
  .back-lockup {
    position: absolute; top: 42px; right: 40px;
    display: flex; align-items: center; gap: 14px;
  }
  .back-lockup .lockup-square { width: 44px; height: 44px; background: var(--accent-blue); }
  .back-lockup .lockup-name {
    color: var(--ink-white); font-weight: 600; font-size: 20px; line-height: 1.1; letter-spacing: 0.5px;
  }
  .holder {
    position: absolute; top: 345px; left: 0; right: 0; text-align: center;
  }
  .holder-name { color: var(--ink-white); font-weight: 700; font-size: 54px; line-height: 1; }
  .holder-role { color: var(--accent-blue); font-weight: 700; font-size: 26px; letter-spacing: 1px; margin-top: 4px; }
  .contact {
    position: absolute; left: 34px; right: 30px; bottom: 40px;
    color: var(--ink-white); font-weight: 600; font-size: 21px; line-height: 1.45; letter-spacing: 0.3px;
  }
  .contact .contact-label { color: var(--accent-blue); margin-right: 4px; }
  .contact .contact-row span + .contact-label { margin-left: 14px; }
  .contact .email { text-transform: lowercase; }
</style>
</head>
<body>
  <main class="sheet">
    <section class="card card-front" aria-label="Card front">
      <div class="front-mark">Corin<br>Vale</div>
      <div class="front-label">
        <span class="label-name">Corin Vale</span>
        <span class="label-sub">Hospitality College</span>
      </div>
    </section>

    <section class="card card-back" aria-label="Card back">
      <div class="back-lockup">
        <span class="lockup-square"></span>
        <span class="lockup-name">Corin Vale<br>Hospitality College</span>
      </div>
      <div class="holder">
        <h1 class="holder-name">Tobin Marsh</h1>
        <p class="holder-role">Director</p>
      </div>
      <div class="contact">
        <p class="contact-row"><span class="contact-label">Phone:</span><span>1300 615 737</span><span class="contact-label">Mobile:</span><span>0455 817 296</span></p>
        <p class="contact-row"><span class="contact-label">Email:</span><span class="email">info@corinvale.example</span></p>
        <p class="contact-row"><span class="contact-label">Website:</span><span class="email">www.corinvale.example</span></p>
      </div>
    </section>
  </main>
</body>
</html>
```